Lip Balm tube design

create label/ product print design for Lip balm tubes
Size of tube
76 mm high
24 mm wide

2.75 x 2" h- this is for the main part of tube, not top cap

Current design has been attached for reference. Would like to stick to something similar but need it to "pop" more and be more readable to user
Designs
Vanilla Mint
Citrus Spice
Coconut Lime
Marshmallow Creme
Satsuma Sugar

Designs must include product information (ingredients) as detailed on examples.
Color palette is color but soft, matte tones

```html
<!DOCTYPE html>
<html lang="en">
<head>
<meta charset="utf-8">
<title>Lip Balm Labels – Marshmallow Creme</title>
<link href="https://fonts.googleapis.com/css2?family=EB+Garamond:wght@400;500&family=Sacramento&display=swap" rel="stylesheet">
<style>
  :root{
    --backdrop:#686b70;
    --cream:#faf2e8;
    --tan:#c8a489;
    --tan-deep:#b89377;
    --tan-soft:#e9d7c6;
  }
  *{box-sizing:border-box;margin:0;padding:0}
  html,body{width:1200px;height:1001px;overflow:hidden;background:var(--backdrop)}
  .canvas{position:relative;width:1200px;height:1001px;background:var(--backdrop)}
  .label{position:absolute;background:var(--cream);overflow:hidden}
  .label--front{left:200px;top:120px;width:240px;height:760px}
  .label--wrap{left:490px;top:182px;width:509px;height:698px}

  .floral{position:absolute;border-radius:50%;
    background:radial-gradient(ellipse at center,var(--tan-soft) 0 45%,rgba(233,215,198,.5) 62%,rgba(250,242,232,0) 72%)}
  .label--front .floral--bottom{left:-40px;top:540px;width:320px;height:260px}
  .label--wrap .floral--bottom{left:-50px;top:480px;width:380px;height:260px}
  .label--wrap .floral--top{left:170px;top:-70px;width:380px;height:260px}

  .name-band{position:absolute;top:0;background:var(--tan);color:var(--cream)}
  .label--front .name-band{left:48px;width:144px;height:566px;border-radius:0 0 72px 72px}
  .label--wrap .name-band{left:52px;width:126px;height:504px;border-radius:0 0 63px 63px}

  .category{position:absolute;border-top:1.5px solid var(--cream);border-bottom:1.5px solid var(--cream);
    font-family:"EB Garamond",serif;text-align:center;letter-spacing:.5px;line-height:1}
  .label--front .category{top:54px;left:18px;right:18px;font-size:21px;padding:7px 0 6px}
  .label--wrap .category{top:44px;left:14px;right:14px;font-size:19px;padding:7px 0 6px}

  .rotated{position:absolute;transform:rotate(-90deg);transform-origin:top left}
  .product-title{display:flex;flex-direction:column}
  .label--front .product-title{left:40px;top:512px;width:394px;height:90px}
  .label--wrap .product-title{left:32px;top:454px;width:348px;height:80px}
  .flavour{font-family:"EB Garamond",serif;font-weight:400;line-height:1;letter-spacing:.5px;white-space:nowrap}
  .label--front .flavour{font-size:49px}
  .label--wrap .flavour{font-size:43px}
  .variant{display:flex;align-items:center;gap:10px;margin-top:-4px}
  .variant-rule{flex:1;height:1.5px;background:var(--cream);margin-left:6px}
  .variant-name{font-family:"Sacramento",cursive;line-height:1;white-space:nowrap}
  .label--front .variant-name{font-size:56px}
  .label--wrap .variant-name{font-size:50px}

  .claims{left:316px;top:680px;width:518px;height:34px;display:flex;justify-content:space-between;
    font-family:"Sacramento",cursive;color:var(--tan);font-size:32px;line-height:1;white-space:nowrap}

  .ingredients{left:364px;top:660px;width:478px;height:68px;font-family:"EB Garamond",serif;
    color:var(--tan-deep);font-size:9.5px;line-height:13px;text-align:center}
  .ingredients-heading{display:block}

  .maker{left:464px;top:654px;width:330px;height:12px;font-family:"EB Garamond",serif;color:var(--tan-deep);
    font-size:8px;line-height:12px;letter-spacing:.2px;white-space:nowrap;display:flex;gap:28px}

  .social{position:absolute;left:462px;top:218px;display:flex;flex-direction:column;gap:12px}
  .social-dot{width:20px;height:20px;border-radius:50%;background:var(--tan)}
</style>
</head>
<body>
<div class="canvas">

  <section class="label label--front">
    <div class="floral floral--bottom" role="img" aria-label="Line-drawn mallow flower with serrated leaves in tan"></div>
    <div class="name-band">
      <div class="category">LIP BALM</div>
      <div class="rotated product-title">
        <span class="flavour">MARSHMALLOW</span>
        <span class="variant"><span class="variant-rule"></span><span class="variant-name">creme</span></span>
      </div>
    </div>
  </section>

  <section class="label label--wrap">
    <div class="floral floral--top" role="img" aria-label="Line-drawn mallow flower with serrated leaves in tan"></div>
    <div class="floral floral--bottom" role="img" aria-label="Line-drawn mallow flower with serrated leaves in tan"></div>
    <div class="name-band">
      <div class="category">LIP BALM</div>
      <div class="rotated product-title">
        <span class="flavour">MARSHMALLOW</span>
        <span class="variant"><span class="variant-rule"></span><span class="variant-name">creme</span></span>
      </div>
    </div>

    <div class="rotated claims">
      <span>plant based</span><span>vegan</span><span>cruelty free</span>
    </div>

    <p class="rotated ingredients">
      <span class="ingredients-heading">Ingredients:</span>
      Organic Olive Fruit Oil (Olea Europaea), Organic Coconut Oil (Cocos Nucifera), Organic Shea Butter (Butyrospermum Parkii), Organic Jojoba Seed Oil (Simmondsia Chinensis), Rosehip Seed Oil (Rosa Canina), Vitamin E (Tocopherol), Sun Flower Oil (Helianthus Annus), Vanilla Aroma, Dipteryx Odorata (Tonka Bean) Oil
    </p>

    <div class="rotated maker">
      <span>WWW.WILLOWMERESOY.CA</span>
      <span>Made by Willowmere Soy, Brookfield, AB T0X 2B4</span>
    </div>

    <div class="social" aria-hidden="true">
      <span class="social-dot"></span>
      <span class="social-dot"></span>
      <span class="social-dot"></span>
    </div>
  </section>

</div>
</body>
</html>
```